This is for a poster that will be hanging in the window of a Men's Suit Store in the mall:
Size 4 feet wide by 6 feet high
Main point is: A sale on "Suits" or "Men's Suits" at 40%-60% off ( the 40%-60% off should be the focal point)
Some words that can be used are "Sale" or "Clearance Sale"
Some key words that can be used to make it urgent are "limited time offer" or something similar.
You can get creative, the point is for the customer to want to come into the store and buy a suit right away.
You may use a graphic (picture of a man in a suit). It is not necessary but if it looks good you can use it. (If you do use a picture, it should be of a modern fit or slim fit suit)
Sorry, the initial brief somehow got deleted from the project. Please see the updated brief.
Thanks
Reason: Project was closed for some reason, extended to give enough time to complete
Target Market(s)
Mostly Men ages 35-55
Industry/Entity Type
Store
Colors
Designer to choose colors to be used in the design.

```html
<!DOCTYPE html>
<html lang="en">
<head>
<meta charset="utf-8">
<title>Marlow Menswear – Men's Suits Clearance Sale</title>
<link rel="stylesheet" href="https://fonts.googleapis.com/css2?family=Archivo+Black&family=Montserrat:wght@600;700;800&family=Open+Sans:wght@300;400&display=swap">
<style>
  :root {
    --page-bg: #f4f4f4;
    --poster-light: #eef1f3;
    --poster-mid: #d9dee2;
    --poster-edge: #bfc6cc;
    --sale-red: #e8302b;
    --figure-face: #e7e9eb;
    --figure-shade: #9aa3ab;
    --ink: #111111;
    --ink-soft: #4a4a4a;
    --wood-light: #ddb084;
    --wood-mid: #c48a52;
    --wood-dark: #a8692f;
  }
  * { margin: 0; padding: 0; box-sizing: border-box; }
  html, body {
    width: 1200px;
    height: 1200px;
    overflow: hidden;
    background: var(--page-bg);
  }
  .poster {
    position: absolute;
    left: 267px;
    top: 60px;
    width: 666px;
    height: 1080px;
    background: radial-gradient(ellipse 70% 55% at 50% 38%, var(--poster-light) 0%, var(--poster-mid) 70%, var(--poster-edge) 100%);
    overflow: hidden;
  }
  .brand {
    position: absolute;
    top: 14px;
    left: 0;
    width: 100%;
    text-align: center;
    font-family: "Open Sans", sans-serif;
    color: var(--ink);
    line-height: 1;
  }
  .brand__name { display: block; font-size: 74px; font-weight: 300; letter-spacing: -1px; }
  .brand__tag { display: block; font-size: 36px; font-weight: 400; margin-top: 0; }
  .hanger-area {
    position: absolute;
    left: 55px;
    top: 158px;
    width: 576px;
    height: 268px;
    border-radius: 24px;
    background: radial-gradient(ellipse 60% 70% at 50% 55%, var(--wood-light) 0%, var(--wood-mid) 55%, var(--wood-dark) 100%);
    opacity: 0.85;
  }
  .discount {
    position: absolute;
    left: 101px;
    top: 398px;
    width: 474px;
    height: 328px;
    background: var(--sale-red);
    box-shadow: 2px 4px 6px rgba(0,0,0,0.2);
    display: flex;
    flex-direction: column;
    align-items: center;
    justify-content: center;
    font-family: "Archivo Black", sans-serif;
    color: var(--figure-face);
    font-size: 160px;
    line-height: 0.86;
    letter-spacing: -2px;
  }
  .discount__figure {
    display: block;
    text-shadow: 5px 4px 0 var(--figure-shade);
  }
  .headline {
    position: absolute;
    left: 0;
    width: 100%;
    text-align: center;
    font-family: "Montserrat", sans-serif;
    line-height: 1;
  }
  .headline--product {
    top: 746px;
    font-size: 52px;
    font-weight: 600;
    color: var(--ink-soft);
  }
  .headline--sale {
    top: 802px;
    font-size: 58px;
    font-weight: 800;
    color: var(--ink);
    letter-spacing: 1.5px;
  }
  .urgency__rule {
    position: absolute;
    top: 990px;
    height: 2px;
    background: var(--ink);
  }
  .urgency__rule--left { left: 2px; width: 162px; }
  .urgency__rule--right { left: 503px; width: 161px; }
  .urgency__icon {
    position: absolute;
    left: 182px;
    top: 942px;
    width: 44px;
    height: 92px;
  }
  .urgency__text {
    position: absolute;
    left: 245px;
    top: 936px;
    font-family: "Montserrat", sans-serif;
    font-weight: 800;
    line-height: 1;
  }
  .urgency__kicker {
    display: block;
    color: var(--sale-red);
    font-size: 31px;
    font-weight: 700;
  }
  .urgency__main {
    display: block;
    color: var(--ink);
    font-size: 70px;
    margin-top: -2px;
    letter-spacing: -2px;
  }
</style>
</head>
<body>
  <main class="poster">
    <header class="brand">
      <span class="brand__name">marlow</span>
      <span class="brand__tag">menswear</span>
    </header>

    <div class="hanger-area" role="img" aria-label="Three stacked wooden coat hangers with silver metal hooks, holding the sale sign"></div>

    <div class="discount" aria-label="40% to 60% off">
      <span class="discount__figure">40%</span>
      <span class="discount__figure">60%</span>
    </div>

    <p class="headline headline--product">Men's Suits</p>
    <p class="headline headline--sale">CLEARANCE SALE</p>

    <div class="urgency__rule urgency__rule--left"></div>
    <div class="urgency__rule urgency__rule--right"></div>

    <svg class="urgency__icon" viewBox="0 0 42 96" preserveAspectRatio="none" aria-hidden="true">
      <rect x="0" y="0" width="42" height="8" rx="2" fill="var(--ink)"/>
      <rect x="0" y="88" width="42" height="8" rx="2" fill="var(--ink)"/>
      <path d="M5 8 H37 C37 30 24 40 24 48 C24 56 37 66 37 88 H5 C5 66 18 56 18 48 C18 40 5 30 5 8 Z" fill="none" stroke="var(--ink)" stroke-width="4"/>
      <path d="M10 14 H32 C31 28 22 36 21 44 C20 36 11 28 10 14 Z" fill="var(--sale-red)"/>
      <path d="M21 60 C26 66 31 74 32 84 H10 C11 74 16 66 21 60 Z" fill="var(--sale-red)"/>
    </svg>

    <p class="urgency__text">
      <span class="urgency__kicker">LIMITED TIME</span>
      <span class="urgency__main">OFFER</span>
    </p>
  </main>
</body>
</html>
```